WordPress Design for both website and landing page for an expert

I need a clean and stylish design for my new website. I work as an expert (see attached file WHY HOW WHAT), my product is expert opinion (reports) for company evaluations You can use all of the attached pictures colored or black / white. The person is me, you can add other pictures, if you want. The design should be clean and stylish, so you could use white, black, gray, silver and / or one additional color. I have added an idea about my website, see attached file CONCEPT WEBSITE If you have any more information, please do not hesitate to contact us 'Hesitate to ask me ...

```html
<!DOCTYPE html>
<html lang="en">
<head>
<meta charset="utf-8">
<title>Elan Varney – Expert for Company Valuations</title>
<link href="https://fonts.googleapis.com/css2?family=Montserrat:wght@400;500;600;700;800&family=Open+Sans:wght@400;600;700&display=swap" rel="stylesheet">
<style>
:root{
  --ink:#151515;
  --black:#0b0b0b;
  --charcoal:#1d1d1f;
  --grey-band:#3a3a3c;
  --grey-text:#555;
  --muted:#8a8a8a;
  --line:#d9d9d9;
  --paper:#ffffff;
  --cream:#f4f1ea;
  --silver:#e8e8ea;
  --sky-top:#2b3d5e;
  --sky-low:#7a8fae;
  --city:#1a2230;
}
*{box-sizing:border-box;margin:0;padding:0}
html,body{width:1200px;height:3956px;overflow:hidden}
body{font-family:"Open Sans",Arial,sans-serif;color:var(--ink);background:var(--paper)}
h1,h2,h3,h4,.nav,.btn,.brand{font-family:"Montserrat",Helvetica,sans-serif}
section{position:relative;width:1200px;overflow:hidden}
.btn{display:inline-block;font-size:11px;font-weight:600;letter-spacing:1px;padding:9px 18px;border:1px solid var(--ink);text-transform:uppercase}
.btn.dark{background:var(--ink);color:#fff}
.btn.ghost{background:transparent;color:var(--ink)}
p{font-size:13px;line-height:1.6;color:var(--grey-text)}

/* Hero */
.hero{height:700px;background:linear-gradient(180deg,var(--sky-top) 0%,#4b6185 35%,var(--sky-low) 55%,#2d3440 70%,var(--city) 100%)}
.hero-photo{position:absolute;inset:0}
.topbar{position:absolute;top:0;left:0;right:0;height:90px;background:rgba(0,0,0,.55);display:flex;align-items:center;padding:0 56px}
.brand{display:flex;flex-direction:column;align-items:center;color:#fff;font-weight:500;letter-spacing:4px;font-size:17px;gap:6px}
.brand .mark{width:28px;height:28px;border:2px solid #fff}
.top-right{margin-left:auto;display:flex;flex-direction:column;align-items:flex-end;gap:14px}
.contact-mini{display:flex;gap:26px;font-size:11px;color:#fff}
.contact-mini span{display:flex;align-items:center;gap:7px}
.nav{display:flex;gap:26px;font-size:11px;font-weight:600;color:#fff;letter-spacing:.5px}
.nav .active{border-bottom:2px solid #fff;padding-bottom:3px}
.hero-title{position:absolute;left:56px;top:530px;color:#fff}
.hero-title h1{font-size:38px;font-weight:700;letter-spacing:1px}
.hero-title h2{font-size:20px;font-weight:600;margin-top:10px;letter-spacing:.5px}

/* What I do */
.what{height:560px;background:var(--paper)}
.what .text{position:absolute;left:56px;top:100px;width:450px}
.what h2{font-size:34px;font-weight:800;margin-bottom:18px}
.what .lead{font-weight:600;color:var(--ink)}
.checks{list-style:none;margin:26px 0 30px}
.checks li{display:flex;gap:14px;align-items:center;font-size:12px;color:var(--grey-text);margin-bottom:14px;line-height:1.4}
.checks svg{flex:none}
.what .photo{position:absolute;right:0;top:90px;width:500px;height:330px;border-radius:40px 0 0 40px;background:linear-gradient(135deg,#e9e4dc,#b7aa97 55%,#6f6255)}

/* Why work with me */
.why{height:560px;background:var(--cream);text-align:center}
.why h2{font-size:32px;font-weight:700;padding-top:90px}
.why .intro{width:640px;margin:16px auto 0;color:var(--ink)}
.why .sub{font-size:12px;margin-top:18px;color:var(--ink)}
.cards{position:absolute;top:368px;left:160px;width:880px;display:flex;justify-content:space-between}
.cards::before{content:"";position:absolute;left:120px;right:120px;top:72px;border-top:1px solid var(--muted)}
.card{position:relative;width:220px;height:145px;background:#fff;border-radius:6px;box-shadow:0 2px 10px rgba(0,0,0,.08);padding:34px 20px 0}
.card .icon{position:absolute;left:50%;top:-30px;transform:translateX(-50%);width:56px;height:56px;border-radius:50%;background:#fff;border:1px solid var(--line);display:flex;align-items:center;justify-content:center}
.card h4{font-size:14px;font-weight:700;margin-bottom:8px}
.card p{font-size:11px;line-height:1.45}

/* Quality promise */
.promise{height:210px;text-align:center;background:var(--paper)}
.promise h2{font-size:32px;font-weight:700;padding-top:40px}
.promise p{margin-top:14px;font-size:15px;color:var(--ink)}
.promise .actions{margin-top:22px;display:flex;gap:14px;justify-content:center}

/* How */
.how{height:610px;background:linear-gradient(160deg,#2c2c2e,#121212 60%,#0a0a0a)}
.how-bg{position:absolute;inset:0}
.how h2{position:relative;color:#fff;text-align:center;font-size:32px;font-weight:700;padding-top:40px}
.lens{position:absolute;left:96px;top:170px;width:340px;height:340px;border-radius:50%;border:10px solid #f1f1f1;background:radial-gradient(circle at 40% 40%,#ffffff,#dfe7f0 60%,#aab9cc)}
.pills{position:absolute;left:330px;top:140px;width:680px}
.pill{position:relative;height:110px;background:linear-gradient(180deg,#fdfdfd,#cfcfd1);border-radius:0 55px 55px 0;margin-bottom:22px;padding:16px 70px 0 160px}
.pill .dot{position:absolute;left:118px;top:14px;width:30px;height:30px;border-radius:50%;background:var(--ink);display:flex;align-items:center;justify-content:center}
.pill h4{font-size:13px;font-weight:700}
.pill p{font-size:11px;line-height:1.45;color:#333;margin-top:4px}
.pill .next{position:absolute;right:16px;top:38px;width:34px;height:34px;border-radius:50%;background:#fff;display:flex;align-items:center;justify-content:center;box-shadow:0 1px 4px rgba(0,0,0,.2)}

/* About */
.about{height:630px;background:linear-gradient(90deg,#f2f2f2,#ffffff)}
.about .portrait{position:absolute;left:60px;top:60px;width:420px;height:660px;background:linear-gradient(180deg,#d9d9d9,#8c8c8c 45%,#2a2a2a);border-radius:200px 200px 0 0;z-index:2}
.about .text{position:absolute;left:560px;top:90px;width:560px}
.about h2{font-size:34px;font-weight:800;margin-bottom:18px}
.about .lead{font-size:16px;font-weight:600;color:var(--ink);line-height:1.5;margin-bottom:18px}
.about p+p{margin-top:14px}
.about .actions{margin-top:24px;display:flex;gap:14px}
.partners{height:90px;background:var(--grey-band);display:flex;align-items:center;padding-left:560px;gap:24px}
.partners h4{color:#fff;font-size:11px;font-weight:600;letter-spacing:1px}
.partners .badge{width:110px;height:46px;background:#fff;border-radius:3px}
.partners .badge.alt{background:#dfe4ec}

/* Contact */
.contact{height:540px;background:var(--black);color:#fff}
.contact h2{text-align:center;font-size:32px;font-weight:700;padding-top:40px}
.contact .info{position:absolute;left:56px;top:170px;width:300px}
.contact .info .brand{align-items:flex-start;margin-bottom:22px}
.contact .info p{color:#bbb;font-size:12px}
.contact .info .line{display:flex;gap:8px;align-items:center;font-size:12px;color:#ddd;margin-top:10px}
.contact .round{position:absolute;left:450px;top:150px;width:300px;height:300px;border-radius:50%;border:8px solid #fff;background:linear-gradient(180deg,#cfcfcf,#555 60%,#222)}
.form{position:absolute;left:790px;top:150px;width:340px}
.form h4{font-size:14px;font-weight:600;letter-spacing:1px;margin-bottom:14px}
.field{border:1px solid #666;height:40px;margin-bottom:12px;font-size:10px;color:#aaa;padding:13px 12px;letter-spacing:1px}
.field.msg{height:90px}
.form .btn{background:#fff;color:var(--ink);border-color:#fff;margin-top:4px}
.footer{height:56px;background:#1a1a1a;color:#999;text-align:center;font-size:11px;line-height:56px;letter-spacing:1px}
</style>
</head>
<body>

<section class="hero">
  <div class="hero-photo" role="img" aria-label="Evening city skyline by a river with a tall tower and lights reflecting on water"></div>
  <header class="topbar">
    <div class="brand"><span class="mark"></span>ELAN VARNEY</div>
    <div class="top-right">
      <div class="contact-mini">
        <span><svg width="12" height="12" viewBox="0 0 24 24"><path d="M6 2h4l2 5-3 2a12 12 0 0 0 6 6l2-3 5 2v4a2 2 0 0 1-2 2A18 18 0 0 1 4 4a2 2 0 0 1 2-2z" fill="#fff"/></svg>+49 211 555 0148</span>
        <span><svg width="13" height="10" viewBox="0 0 26 20"><rect x="1" y="1" width="24" height="18" fill="none" stroke="#fff" stroke-width="2"/><path d="M1 1l12 10L25 1" fill="none" stroke="#fff" stroke-width="2"/></svg>info@elanvarney-example.com</span>
      </div>
      <nav class="nav"><span class="active">HOME</span><span>WHAT I DO</span><span>WHY I DO IT &amp; HOW I DO IT</span><span>ABOUT ME</span><span>CONTACT</span></nav>
    </div>
  </header>
  <div class="hero-title">
    <h1>EXPERT FOR COMPANY VALUATIONS</h1>
    <h2>YOU NEED AN OPINION TO DETERMINE THE VALUE OF YOUR COMPANY</h2>
  </div>
</section>

<section class="what">
  <div class="text">
    <h2>WHAT I DO</h2>
    <p class="lead">Lorem Ipsum is simply dummy text of the printing and typesetting industry. Lorem Ipsum has been the industry's standard dummy text ever since the 1500s, when an unknown printer took a galley of type and scrambled it to make a type specimen book.</p>
    <ul class="checks">
      <li><svg width="26" height="26" viewBox="0 0 26 26"><circle cx="13" cy="13" r="12" fill="none" stroke="#151515"/><path d="M8 13l4 4 7-8" fill="none" stroke="#151515" stroke-width="1.6"/></svg>Handling of enterprise records at Purchase / Sale of Ventures or Complete Business</li>
      <li><svg width="26" height="26" viewBox="0 0 26 26"><circle cx="13" cy="13" r="12" fill="none" stroke="#151515"/><path d="M8 13l4 4 7-8" fill="none" stroke="#151515" stroke-width="1.6"/></svg>Handling of enterprise records at Purchase / Sale of Ventures or Complete Business</li>
      <li><svg width="26" height="26" viewBox="0 0 26 26"><circle cx="13" cy="13" r="12" fill="none" stroke="#151515"/><path d="M8 13l4 4 7-8" fill="none" stroke="#151515" stroke-width="1.6"/></svg>Handling of enterprise records at Questions in the Home (at separation)</li>
    </ul>
    <span class="btn dark">Learn more</span> <span class="btn ghost">Contact us</span>
  </div>
  <div class="photo" role="img" aria-label="Hand signing a valuation document at a desk"></div>
</section>

<section class="why">
  <h2>WHY YOU SHOULD WORK WITH ME</h2>
  <p class="intro">Lorem Ipsum is simply dummy text of the printing and typesetting industry. Lorem Ipsum has been the industry's standard dummy text ever since the 1500s, when an unknown printer took a galley of type and scrambled it to make a type specimen book.</p>
  <p class="sub">3 reasons, why you should work with me</p>
  <div class="cards">
    <div class="card">
      <div class="icon"><svg width="28" height="28" viewBox="0 0 28 28"><circle cx="14" cy="14" r="11" fill="none" stroke="#151515" stroke-width="1.6"/><path d="M14 7v7l5 3" fill="none" stroke="#151515" stroke-width="1.6"/></svg></div>
      <h4>SCHNELL</h4>
      <p>You will find your guidance within max. 21 days with to every need.</p>
    </div>
    <div class="card">
      <div class="icon"><svg width="28" height="28" viewBox="0 0 28 28"><rect x="5" y="4" width="18" height="20" fill="none" stroke="#151515" stroke-width="1.6"/><path d="M9 14l4 4 6-7" fill="none" stroke="#151515" stroke-width="1.6"/></svg></div>
      <h4>CERTIFIED</h4>
      <p>They receive our qualified and valued benefit from a certified expert (highest acceptance at all parties).</p>
    </div>
    <div class="card">
      <div class="icon"><svg width="28" height="28" viewBox="0 0 28 28"><path d="M14 23S4 16 4 10a5 5 0 0 1 10-1 5 5 0 0 1 10 1c0 6-10 13-10 13z" fill="none" stroke="#151515" stroke-width="1.6"/></svg></div>
      <h4>SENSITIVE</h4>
      <p>Our guests are logical and can be well for you, and do not consider "chinese".</p>
    </div>
  </div>
</section>

<section class="promise">
  <h2>MY QUALITY PROMISE</h2>
  <p>should the advised date for the preparation of the report be exceeded, you will<br>receive the report free of charge (I waive my fee)</p>
  <div class="actions"><span class="btn dark">Learn more</span><span class="btn ghost">Contact us</span></div>
</section>

<section class="how">
  <div class="how-bg" role="img" aria-label="Dark office background with papers and reports"></div>
  <h2>WHY I DO IT &amp; HOW I DO IT</h2>
  <div class="lens" role="img" aria-label="Magnifying glass over a financial chart"></div>
  <div class="pills">
    <div class="pill"><span class="dot"><svg width="12" height="12" viewBox="0 0 12 12"><circle cx="6" cy="6" r="3" fill="#fff"/></svg></span><h4>WHY</h4><p>Around economy is my passion. Economy is made in numbers. Sometimes it is difficult to find the right numbers. I am always interested in finding out how economy works and which numbers will tell the reality true story.</p><span class="next"><svg width="12" height="12" viewBox="0 0 12 12"><path d="M4 2l4 4-4 4" fill="none" stroke="#151515" stroke-width="1.6"/></svg></span></div>
    <div class="pill"><span class="dot"><svg width="12" height="12" viewBox="0 0 12 12"><circle cx="6" cy="6" r="3" fill="#fff"/></svg></span><h4>HOW</h4><p>Each matter starts with understanding. So I ask you and listen very carefully. In the preparation of each report I follow one defined process, but which is tailored to the particular entity company is concerned.</p></div>
    <div class="pill"><span class="dot"><svg width="12" height="12" viewBox="0 0 12 12"><circle cx="6" cy="6" r="3" fill="#fff"/></svg></span><h4>WHAT</h4><p>Conducting business valuation in case of handling of enterprise records (Vaulting). "Scaling" selling shares or entire companies. Inheritance matters.</p></div>
  </div>
</section>

<section class="about">
  <div class="portrait" role="img" aria-label="Black and white full-length portrait of the expert in a dark suit holding a folder"></div>
  <div class="text">
    <h2>ABOUT ME</h2>
    <p class="lead">Lorem Ipsum has been the industry's standard dummy text ever since the 1500s, when an unknown printer took a galley of type and scrambled it to make a type specimen book.</p>
    <p>Lorem Ipsum is simply dummy text of the printing and typesetting industry. Lorem Ipsum has been the industry's standard dummy text ever since the 1500s, when an unknown printer took a galley of type and scrambled it to make a type specimen book.</p>
    <p>Lorem Ipsum is simply dummy text of the printing and typesetting industry. Lorem Ipsum has been the industry's standard dummy text ever since the 1500s, when an unknown printer took a galley of type and scrambled it to make a type specimen book.</p>
    <p>When an unknown printer took a galley of type and scrambled it to make a type specimen book.</p>
    <div class="actions"><span class="btn dark">Learn more</span><span class="btn ghost">Contact us</span></div>
  </div>
</section>
<section class="partners">
  <h4>LINKS / PARTNERS</h4>
  <span class="badge alt"></span>
  <span class="badge"></span>
</section>

<section class="contact">
  <h2>GET IN TOUCH</h2>
  <div class="info">
    <div class="brand"><span class="mark"></span>ELAN VARNEY</div>
    <p>Nam libero tempore, cum soluta nobis est eligendi optio cumque nihil impedit quo minus id quod maxime.</p>
    <div class="line" style="margin-top:18px">Varney Valuation GmbH<br>Uferstraße 18, 40210 Rheinstadt</div>
    <div class="line"><svg width="12" height="12" viewBox="0 0 24 24"><path d="M6 2h4l2 5-3 2a12 12 0 0 0 6 6l2-3 5 2v4a2 2 0 0 1-2 2A18 18 0 0 1 4 4a2 2 0 0 1 2-2z" fill="#fff"/></svg>+49 211 555 0148</div>
    <div class="line"><svg width="13" height="10" viewBox="0 0 26 20"><rect x="1" y="1" width="24" height="18" fill="none" stroke="#fff" stroke-width="2"/><path d="M1 1l12 10L25 1" fill="none" stroke="#fff" stroke-width="2"/></svg>info@elanvarney-example.com</div>
  </div>
  <div class="round" role="img" aria-label="Round black and white portrait of the expert in a suit"></div>
  <div class="form">
    <h4>MESSAGE ME</h4>
    <div class="field">NAME *</div>
    <div class="field">SUBJECT *</div>
    <div class="field msg">MESSAGE *</div>
    <span class="btn">Submit</span>
  </div>
</section>
<footer class="footer">COPYRIGHT © 2019 ELAN VARNEY. ALL RIGHTS RESERVED.</footer>

</body>
</html>
```